Company notecard redesign

We'd like a redesign done of our company notecards. We use these cards to hand-write messages to clients/potential clients. This could be thank-you cards, congratulations cards, check-in cards, etc. Current cards are 5.5" x 8.5" and fold in half (you'll see the fold mark on the scanned image). We would like the new cards to not fold, and just be 5.5" x 4.25". We do like the little dog head you'll see on the inside notecard scan as the dog is our logo. I've also attached our "professional" logo with our new tagline. Address info you see on the outside notecard scan is correct.

Target Market(s)

Brindlequay and CRM clients

Industry/Entity Type

It Company

Colors
3377b5
ffffff
fff8ef

Requirements
Must have
• Our logo, some contact info
Nice to have
• Dog head from our current notecard scan

```html
<!DOCTYPE html>
<html lang="en">
<head>
<meta charset="utf-8">
<title>Northwick Notecard</title>
<link href="https://fonts.googleapis.com/css2?family=Montserrat:wght@600;700&family=Oswald:wght@300&family=Open+Sans:wght@400&display=swap" rel="stylesheet">
<style>
  :root {
    --stage: #e9e9e9;
    --card-dark: #0b0f12;
    --card-light: #ffffff;
    --brand-blue: #7fb0cc;
    --rule-blue: #3377b5;
    --hello-white: #ffffff;
  }
  * { box-sizing: border-box; margin: 0; padding: 0; }
  html, body {
    width: 1200px; height: 720px; overflow: hidden;
    background: var(--stage);
  }
  .canvas {
    position: relative; width: 1200px; height: 720px;
    display: flex; align-items: center; justify-content: center; gap: 60px;
  }
  .notecard {
    position: relative; width: 520px; height: 402px;
    box-shadow: 0 2px 6px rgba(0,0,0,0.18);
  }
  .notecard--front { background: var(--card-dark); }
  .notecard--back { background: var(--card-light); }

  .greeting {
    position: absolute; top: 96px; left: 0; right: 0;
    text-align: center;
  }
  .greeting__word {
    display: inline-block;
    font-family: "Montserrat", sans-serif; font-weight: 700;
    font-size: 19px; letter-spacing: 2px; color: var(--hello-white);
    padding: 0 12px 6px;
    border-bottom: 1px solid var(--rule-blue);
  }

  .contact {
    position: absolute; left: 34px; bottom: 92px;
    display: flex; gap: 16px;
    font-family: "Oswald", sans-serif; font-weight: 300;
    font-size: 14px; letter-spacing: 0.3px; color: var(--brand-blue);
    text-transform: uppercase;
  }

  .brand {
    position: absolute; right: 34px; bottom: 28px;
    display: flex; flex-direction: column; align-items: flex-end;
  }
  .brand__row { display: flex; align-items: center; gap: 8px; }
  .brand__square {
    width: 12px; height: 12px;
    background: var(--rule-blue);
  }
  .brand__name {
    font-family: "Montserrat", sans-serif; font-weight: 600;
    font-size: 22px; line-height: 1; letter-spacing: 0;
    color: var(--hello-white);
  }
  .brand__tagline {
    margin-top: 6px;
    font-family: "Open Sans", sans-serif; font-size: 10px;
    letter-spacing: 0.3px; color: var(--brand-blue);
  }

  .mascot-art {
    position: absolute; right: 0; bottom: 0;
    width: 200px; height: 170px;
    background: var(--brand-blue);
    border-top-left-radius: 90px 80px;
  }
</style>
</head>
<body>
  <main class="canvas">
    <section class="notecard notecard--front" aria-label="Notecard front">
      <div class="greeting"><span class="greeting__word">HELLO</span></div>
      <p class="contact">
        <span class="contact__web">northwick.example</span>
        <span class="contact__phone">555.014.2290</span>
        <span class="contact__address">1180 W Orchard Ln Fairview IN 46000</span>
      </p>
      <div class="brand">
        <div class="brand__row">
          <span class="brand__square"></span>
          <span class="brand__name">Northwick</span>
        </div>
        <span class="brand__tagline">Cloud advisory for growing teams</span>
      </div>
    </section>

    <section class="notecard notecard--back" aria-label="Notecard back">
      <div class="mascot-art" role="img" aria-label="Light blue illustration of the company's dog mascot head in profile, looking up"></div>
    </section>
  </main>
</body>
</html>
```